Bref créative
Business Card, Stationary, and #10 Envelope
Bright Harbor Advising
I need double sided standard sized Business Card [3.5" x 2"]
Logo font was Brussels, please use the same, similar or compatible font
Professional
Milo Trenholt
Certified College Planning Specialist
4870 Quarlow Lane
Corvane, Elmshire 58246
milo@brightharboradvising.example
www.brightharboradvising.example
Would like the colors of the card to match the logo. Gold/yellow, black, and white. 2 designs are included, one with a gold tag line, and one with a black tag line. I prefer the gold tag line so I am hoping your designs can utilize that coloring but I am open to ideas.
We can help you:
-Afford college while protecting retirement
-Lower the total cost of college
-Maximize financial aid qualification
-Compare the net cost of public vs private schools
Logo
Logo 2

```html
<!DOCTYPE html>
<html lang="en">
<head>
<meta charset="utf-8">
<title>Bright Harbor Advising – Business Cards</title>
<link rel="stylesheet" href="https://fonts.googleapis.com/css2?family=Libre+Baskerville:wght@700&family=Arimo:ital,wght@0,400;0,700;1,700&display=swap">
<style>
  :root {
    --gold: #e8b21e;
    --gold-deep: #c8930c;
    --ink: #111111;
    --paper: #ffffff;
    --grey-text: #333333;
    --backdrop: #e9e7e3;
  }
  * { margin: 0; padding: 0; box-sizing: border-box; }
  html, body { width: 1200px; height: 850px; overflow: hidden; }
  body { background: var(--backdrop); font-family: "Arimo", Arial, sans-serif; position: relative; }

  .card {
    position: absolute; width: 470px; height: 268px; border-radius: 14px; overflow: hidden;
    box-shadow: 0 6px 18px rgba(0,0,0,.25);
  }
  .card--light { background: var(--paper); color: var(--grey-text); }
  .card--dark { background: linear-gradient(160deg, #2b2b2b 0%, #0b0b0b 55%, #000 100%); color: #f2f2f2; }
  .pos-a { left: 110px; top: 120px; }
  .pos-b { left: 620px; top: 120px; }
  .pos-c { left: 110px; top: 460px; }
  .pos-d { left: 620px; top: 460px; }

  .brand { position: absolute; left: 26px; top: 30px; display: flex; align-items: center; gap: 12px; }
  .brand-dot { width: 44px; height: 44px; border-radius: 50%; background: var(--gold); flex: none; }
  .brand-name { font-family: "Libre Baskerville", Georgia, serif; font-weight: 700; font-size: 25px; color: var(--ink); white-space: nowrap; }
  .card--dark .brand-name { color: #ffffff; }
  .tagline {
    position: absolute; left: 82px; top: 80px; font-size: 9.5px; font-style: italic; font-weight: 700;
    color: var(--gold-deep); letter-spacing: .3px; white-space: nowrap;
  }
  .card--dark .tagline { color: var(--gold); }
  .divider { position: absolute; left: 160px; top: 112px; width: 1px; height: 72px; background: #9a9a9a; }
  .card--dark .divider { background: #777; }
  .person { position: absolute; left: 28px; top: 124px; width: 128px; text-align: center; }
  .person-name { font-size: 14px; font-weight: 700; color: var(--gold-deep); }
  .card--dark .person-name { color: var(--gold); }
  .person-title { font-size: 7.5px; margin-top: 2px; white-space: nowrap; }
  .contact { position: absolute; left: 172px; top: 116px; font-size: 8.5px; line-height: 12px; white-space: nowrap; }
  .contact-gap { height: 8px; }
  .contact-row { display: flex; align-items: center; gap: 5px; }
  .contact-row svg { width: 8px; height: 8px; flex: none; }
  .swoosh { position: absolute; left: 0; bottom: 0; width: 470px; height: 80px; }
  .website { position: absolute; right: 22px; bottom: 10px; font-size: 8px; color: #ffffff; }

  .photo-area { position: absolute; right: 0; top: 0; width: 250px; height: 268px;
    background: linear-gradient(90deg, rgba(200,200,200,0) 0%, rgba(170,170,170,.55) 45%, rgba(120,120,120,.35) 100%); }
  .card--dark .photo-area { background: linear-gradient(90deg, rgba(60,60,60,0) 0%, rgba(110,110,110,.5) 45%, rgba(70,70,70,.3) 100%); }
  .back-mark { position: absolute; left: 34px; top: 26px; width: 80px; height: 80px; border-radius: 50%; background: var(--gold); }
  .card--light .back-mark { background: var(--ink); }
  .help { position: absolute; left: 30px; top: 150px; }
  .help-title { font-size: 11px; font-weight: 700; color: var(--ink); margin-bottom: 6px; }
  .card--dark .help-title { color: var(--gold); }
  .help-list { list-style: none; font-size: 10px; line-height: 15.5px; color: var(--ink); }
  .card--dark .help-list { color: #ffffff; }
  .help-list li { display: flex; align-items: center; gap: 7px; white-space: nowrap; }
  .help-list svg { width: 9px; height: 9px; flex: none; }
</style>
</head>
<body>

<section class="card card--light pos-a">
  <div class="brand"><span class="brand-dot"></span><span class="brand-name">Bright Harbor Advising</span></div>
  <p class="tagline">PLAN AHEAD, AND PLAN IT WELL</p>
  <div class="person"><p class="person-name">Milo Trenholt</p><p class="person-title">Certified College Planning Specialist</p></div>
  <div class="divider"></div>
  <div class="contact">
    <p>4870 Quarlow Lane</p><p>Corvane, Elmshire 58246</p>
    <div class="contact-gap"></div>
    <p class="contact-row"><svg viewBox="0 0 10 10"><circle cx="5" cy="5" r="5" fill="#111"/><path d="M3 3l1 0 .6 1.3-.6.5a3 3 0 0 0 1.3 1.3l.5-.6 1.3.6 0 1c-2.5 0-4.1-1.6-4.1-4.1z" fill="#fff"/></svg>701-555-0142</p>
    <p class="contact-row"><svg viewBox="0 0 10 10"><circle cx="5" cy="5" r="5" fill="#111"/><path d="M3 3l1 0 .6 1.3-.6.5a3 3 0 0 0 1.3 1.3l.5-.6 1.3.6 0 1c-2.5 0-4.1-1.6-4.1-4.1z" fill="#fff"/></svg>888-555-0187</p>
    <p class="contact-row"><svg viewBox="0 0 10 10"><circle cx="5" cy="5" r="5" fill="#111"/><rect x="2.6" y="3.4" width="4.8" height="3.4" fill="none" stroke="#fff" stroke-width=".7"/><path d="M2.6 3.4L5 5.3 7.4 3.4" fill="none" stroke="#fff" stroke-width=".7"/></svg>milo@brightharboradvising.example</p>
  </div>
  <svg class="swoosh" viewBox="0 0 470 80" preserveAspectRatio="none">
    <path d="M0 20 C120 70 300 50 470 30 L470 80 L0 80 Z" fill="#111"/>
    <path d="M0 38 C140 80 320 58 470 48 L470 80 L0 80 Z" fill="#e8b21e"/>
    <path d="M0 52 C150 88 330 66 470 62 L470 80 L0 80 Z" fill="#c8930c"/>
  </svg>
  <p class="website">www.brightharboradvising.example</p>
</section>

<section class="card card--dark pos-b">
  <div class="brand"><span class="brand-dot"></span><span class="brand-name">Bright Harbor Advising</span></div>
  <p class="tagline">PLAN AHEAD, AND PLAN IT WELL</p>
  <div class="person"><p class="person-name">Milo Trenholt</p><p class="person-title">Certified College Planning Specialist</p></div>
  <div class="divider"></div>
  <div class="contact">
    <p>4870 Quarlow Lane</p><p>Corvane, Elmshire 58246</p>
    <div class="contact-gap"></div>
    <p class="contact-row"><svg viewBox="0 0 10 10"><circle cx="5" cy="5" r="5" fill="#fff"/><path d="M3 3l1 0 .6 1.3-.6.5a3 3 0 0 0 1.3 1.3l.5-.6 1.3.6 0 1c-2.5 0-4.1-1.6-4.1-4.1z" fill="#111"/></svg>701-555-0142</p>
    <p class="contact-row"><svg viewBox="0 0 10 10"><circle cx="5" cy="5" r="5" fill="#fff"/><path d="M3 3l1 0 .6 1.3-.6.5a3 3 0 0 0 1.3 1.3l.5-.6 1.3.6 0 1c-2.5 0-4.1-1.6-4.1-4.1z" fill="#111"/></svg>888-555-0187</p>
    <p class="contact-row"><svg viewBox="0 0 10 10"><circle cx="5" cy="5" r="5" fill="#fff"/><rect x="2.6" y="3.4" width="4.8" height="3.4" fill="none" stroke="#111" stroke-width=".7"/><path d="M2.6 3.4L5 5.3 7.4 3.4" fill="none" stroke="#111" stroke-width=".7"/></svg>milo@brightharboradvising.example</p>
  </div>
  <svg class="swoosh" viewBox="0 0 470 80" preserveAspectRatio="none">
    <path d="M0 20 C120 70 300 50 470 30 L470 80 L0 80 Z" fill="#ffffff"/>
    <path d="M0 38 C140 80 320 58 470 48 L470 80 L0 80 Z" fill="#e8b21e"/>
    <path d="M0 52 C150 88 330 66 470 62 L470 80 L0 80 Z" fill="#c8930c"/>
  </svg>
  <p class="website">www.brightharboradvising.example</p>
</section>

<section class="card card--light pos-c">
  <div class="photo-area" role="img" aria-label="Faded photo of a graduate in cap and gown throwing a cap"></div>
  <div class="back-mark"></div>
  <div class="help">
    <p class="help-title">WE CAN HELP YOU :</p>
    <ul class="help-list">
      <li><svg viewBox="0 0 10 10"><path d="M1 5l3 3 5-7" fill="none" stroke="#e8b21e" stroke-width="2"/></svg>Afford college while protecting retirement</li>
      <li><svg viewBox="0 0 10 10"><path d="M1 5l3 3 5-7" fill="none" stroke="#e8b21e" stroke-width="2"/></svg>Lower the total cost of college</li>
      <li><svg viewBox="0 0 10 10"><path d="M1 5l3 3 5-7" fill="none" stroke="#e8b21e" stroke-width="2"/></svg>Maximize financial aid qualification</li>
      <li><svg viewBox="0 0 10 10"><path d="M1 5l3 3 5-7" fill="none" stroke="#e8b21e" stroke-width="2"/></svg><span>Compare the <b>net</b> cost of public vs private schools</span></li>
    </ul>
  </div>
</section>

<section class="card card--dark pos-d">
  <div class="photo-area" role="img" aria-label="Faded photo of a graduate in cap and gown throwing a cap"></div>
  <div class="back-mark"></div>
  <div class="help">
    <p class="help-title">WE CAN HELP YOU :</p>
    <ul class="help-list">
      <li><svg viewBox="0 0 10 10"><path d="M1 5l3 3 5-7" fill="none" stroke="#e8b21e" stroke-width="2"/></svg>Afford college while protecting retirement</li>
      <li><svg viewBox="0 0 10 10"><path d="M1 5l3 3 5-7" fill="none" stroke="#e8b21e" stroke-width="2"/></svg>Lower the total cost of college</li>
      <li><svg viewBox="0 0 10 10"><path d="M1 5l3 3 5-7" fill="none" stroke="#e8b21e" stroke-width="2"/></svg>Maximize financial aid qualification</li>
      <li><svg viewBox="0 0 10 10"><path d="M1 5l3 3 5-7" fill="none" stroke="#e8b21e" stroke-width="2"/></svg><span>Compare the <b>net</b> cost of public vs private schools</span></li>
    </ul>
  </div>
</section>

</body>
</html>
```